Standout Plastic Packaging for a Natural Air Purifying Product!

Hello, we are Brindlewick Home Co. and this packaging design will be for our multipurpose 8-pack of Natural Air Purifiers.

We are listing our products for sale online, and its a very crowded marketplace, so we are looking for a stand-out, colourful, on-brand approach to our packaging design.

- Refer to "design template for package" file for actual template of packaging to be printed. We cannot do any other size; final design must be on this template provided.

- We would like the front of our packaging to be an extended version of our logo design; so I have attached AI logo files to make this happen.

- We are aiming for a minimalistic, symmetrical, on-brand design to host our premium homeware brand designed for American's.

- Refer to the "MOCKUP_front" and "MOCKUP_back" files for all of the preferred text, colours, and overall concept we have in mind.

Looking forward to seeing your ideas! :)

BRAND COLOUR CODES:
#e7948a
#f8b195
#f3e1d8
#f67280
#c06c84
#6c5b7b
#355c7d
#274357

BRAND FONTS:
Raleway
Quickbrush
Sifonn Outline
Montserrat
Updates

Target Market(s)

Vendora shoppers, women aged 27-55, located in the USA

Font styles to use
Other font styles liked:
• Raleway, Quickbrush, Sifonn Outline, Montserrat

Requirements
Must have
• - Brand colours (see project description)
• - Extend logo to suit packaging template provided
• - Refer to front and back mockup files attached
• - Minimal & symmetrical design
• - Symbol for 8 PACK
• - Space for barcode on rear
Nice to have
• Refer to mockup file attached

```html
<!DOCTYPE html>
<html lang="en">
<head>
<meta charset="utf-8">
<title>Brindlewick Home Co. – Natural Air Purifiers Pouch</title>
<link rel="stylesheet" href="https://fonts.googleapis.com/css2?family=Raleway:wght@400;500;600;700&family=Montserrat:wght@400;500;700;800&display=swap">
<style>
  :root {
    --coral: #e7948a;
    --peach: #f8b195;
    --blush: #f3e1d8;
    --rose: #f67280;
    --mauve: #c06c84;
    --plum: #6c5b7b;
    --slate: #355c7d;
    --navy: #274357;
    --ink: #3b3550;
    --paper: #ececec;
    --white: #ffffff;
  }
  * { box-sizing: border-box; margin: 0; padding: 0; }
  html, body { width: 1200px; height: 952px; overflow: hidden; }
  body {
    background: var(--paper);
    font-family: "Raleway", sans-serif;
    position: relative;
  }
  .pouch {
    position: absolute;
    top: 166px;
    width: 464px;
    height: 614px;
    overflow: hidden;
  }
  .pouch--front { left: 112px; }
  .pouch--back { left: 636px; }

  .front-scene {
    position: absolute; inset: 0;
    background: linear-gradient(180deg,
      var(--blush) 0%, #f6d3c8 18%, var(--coral) 32%, #ec8a86 44%,
      var(--mauve) 54%, var(--plum) 64%, var(--slate) 74%, var(--navy) 86%, var(--navy) 100%);
  }
  .pack-badge {
    position: absolute; top: 16px;
    width: 76px; height: 76px; border-radius: 50%;
    background: var(--rose);
    color: var(--white);
    font-family: "Montserrat", sans-serif; font-weight: 700; font-size: 15px;
    display: flex; align-items: center; justify-content: center;
  }
  .pouch--front .pack-badge { left: 18px; }
  .pouch--back .pack-badge { right: 18px; }

  .centered { position: absolute; left: 0; right: 0; text-align: center; }

  .brand-name {
    top: 322px; color: var(--white);
    font-family: "Raleway", sans-serif; font-weight: 500; font-size: 52px; letter-spacing: 0.5px;
  }
  .brand-sub {
    top: 398px; color: var(--white);
    font-family: "Montserrat", sans-serif; font-weight: 500; font-size: 17px; letter-spacing: 6px;
  }
  .product-line {
    top: 446px; color: var(--peach);
    font-family: "Montserrat", sans-serif; font-weight: 500; font-size: 16px; letter-spacing: 5px;
  }
  .charcoal-band {
    position: absolute; left: 0; right: 0; top: 474px; height: 34px;
    background: var(--peach);
    color: var(--navy);
    font-family: "Montserrat", sans-serif; font-weight: 800; font-size: 16px; letter-spacing: 2px;
    display: flex; align-items: center; justify-content: center;
  }
  .feature-bags {
    top: 523px; color: var(--peach);
    font-family: "Montserrat", sans-serif; font-weight: 500; font-size: 13px; letter-spacing: 1.5px;
  }
  .pack-contents {
    top: 549px; color: var(--peach);
    font-family: "Montserrat", sans-serif; font-size: 10px;
  }
  .benefits {
    top: 573px; color: var(--peach);
    font-family: "Montserrat", sans-serif; font-weight: 400; font-size: 13.5px; letter-spacing: 1.2px;
  }

  /* back */
  .back-field {
    position: absolute; inset: 0;
    background: linear-gradient(180deg, #f5e0d8 0%, var(--blush) 30%, #f4d7cd 60%, #f2cfc3 78%);
  }
  .back-base {
    position: absolute; left: 0; right: 0; top: 506px; bottom: 0;
    background: var(--navy);
  }
  .logo-mark {
    position: absolute; left: 50%; top: 38px; transform: translateX(-50%);
    width: 64px; height: 64px; border-radius: 50%; background: var(--coral);
  }
  .back-name {
    top: 112px; color: var(--navy);
    font-weight: 500; font-size: 26px;
  }
  .back-sub {
    top: 144px; color: var(--navy);
    font-family: "Montserrat", sans-serif; font-size: 8px; letter-spacing: 3px;
  }
  .impurities {
    position: absolute; left: 48px; top: 196px; width: 132px;
    color: var(--ink); font-family: "Montserrat", sans-serif;
  }
  .impurities h2 {
    font-size: 11.5px; font-weight: 500; text-align: center; line-height: 1.55; margin-bottom: 12px;
  }
  .impurities ul { list-style: none; padding-left: 8px; }
  .impurities li { font-size: 11.5px; color: var(--plum); line-height: 19px; }
  .impurities li::before { content: "•"; margin-right: 2px; }
  .charcoal-photo {
    position: absolute; left: 228px; top: 172px; width: 192px; height: 192px; border-radius: 50%;
    border: 6px solid var(--slate);
    background: radial-gradient(circle at 45% 40%, #5e6470 0%, #33363e 55%, #1d1f25 100%);
    display: flex; align-items: center; justify-content: center; text-align: center;
    color: var(--white); font-family: "Montserrat", sans-serif; font-weight: 700; font-size: 11px; letter-spacing: 1px; line-height: 1.35;
  }
  .claim {
    color: var(--plum); font-family: "Montserrat", sans-serif; font-weight: 500; font-size: 12.5px; letter-spacing: 0.8px;
  }
  .claim--safe { top: 396px; }
  .claim--healthy { top: 419px; }
  .see-inside {
    top: 464px; color: var(--navy);
    font-family: "Montserrat", sans-serif; font-weight: 500; font-size: 9.5px;
  }
  .info-band {
    position: absolute; left: 0; right: 0; top: 476px; height: 32px;
    background: var(--coral);
    color: var(--navy); font-family: "Montserrat", sans-serif; font-size: 9.5px; line-height: 13px;
    display: flex; align-items: center; justify-content: center; text-align: center;
  }
  .support-title { top: 520px; color: var(--peach); font-family: "Montserrat", sans-serif; font-weight: 500; font-size: 10px; }
  .support-mail { top: 534px; color: var(--peach); font-family: "Montserrat", sans-serif; font-size: 10.5px; }
  .support-mail strong { font-weight: 500; }
  .social {
    position: absolute; left: 20px; top: 574px;
    color: var(--plum); font-family: "Montserrat", sans-serif; font-size: 8px;
  }
  .origin {
    position: absolute; left: 0; right: 0; top: 590px; text-align: center;
    color: var(--plum); font-family: "Montserrat", sans-serif; font-size: 8.5px;
  }
</style>
</head>
<body>

<section class="pouch pouch--front" aria-label="Front of pouch">
  <div class="front-scene" role="img" aria-label="Layered watercolour mountain range under a pale sun, fading from coral peaks to navy foothills"></div>
  <div class="pack-badge">8 PACK</div>
  <h1 class="centered brand-name">Brindlewick</h1>
  <p class="centered brand-sub">HOME CO.</p>
  <p class="centered product-line">NATURAL AIR PURIFIERS</p>
  <div class="charcoal-band">100% BAMBOO CHARCOAL</div>
  <p class="centered feature-bags">BREATHABLE LINEN BAGS</p>
  <p class="centered pack-contents">Multipurpose pack includes: 1 x 500g, 2 x 200g, 1 x 100g, 4 x 50g</p>
  <p class="centered benefits">ALL NATURAL • PET FRIENDLY • USE FOR 2 YEARS</p>
</section>

<section class="pouch pouch--back" aria-label="Back of pouch">
  <div class="back-field"></div>
  <div class="back-base"></div>
  <div class="pack-badge">8 PACK</div>
  <div class="logo-mark"></div>
  <p class="centered back-name">Brindlewick</p>
  <p class="centered back-sub">HOME CO.</p>

  <div class="impurities">
    <h2>ABSORB &amp; ELIMINATE IMPURITIES</h2>
    <ul>
      <li>HARMFUL TOXINS</li>
      <li>ODORS</li>
      <li>MOISTURE</li>
      <li>MOLD &amp; MILDEW</li>
      <li>ALLERGENS</li>
    </ul>
  </div>

  <div class="charcoal-photo" role="img" aria-label="Close-up photograph of bamboo charcoal pieces">100%<br>BAMBOO CHARCOAL</div>

  <p class="centered claim claim--safe">SAFE ALTERNATIVE TO HARMFUL AIR FRESHENER SPRAYS</p>
  <p class="centered claim claim--healthy">PRODUCES HEALTHY, PURIFIED AIR</p>

  <p class="centered see-inside">SEE INSIDE FOR:</p>
  <div class="info-band">Instructions on where to use, how to reuse for up to 2 years,<br>and how to claim your extended 2 year warranty.</div>

  <p class="centered support-title">NEED SUPPORT?</p>
  <p class="centered support-mail">Email us at <strong>care@brindlewickhome.shop</strong></p>

  <p class="social">@brindlewickhome</p>
  <p class="origin">Made in China</p>
</section>

</body>
</html>
```